Restaurant needs a vertical banner for fried catfish

Our restaurant is looking for an eye-catching 78.75in. x 36in. vertical physical banner ad for our fried catfish. Photos for the fried catfish will be provided as a reference but we will also accept anything similar to the photo. We will be using the following as our receptacle: https://www.plankoria.example/banner-stand/retractable-banner-stands/
The design must incorporate the following flavor texts:
Fried Catfish
Always Fresh!
Made from Scratch
Hand-cut Fillets
The Best Catfish in Texas
Served with fries, hush puppies, and a 32oz fountain drink
Also available by the pound!
The final design should be creative, professional, and eye-catching for customers.
Updates
Colors
Designer to choose colors to be used in the design.
Requirements
Must have
- We are open to any and all design elements, albeit the 'flavor texts' should not overpower, but complement the fried catfish photo. 'Fried Catfish' can be used in lieu of a main title/logo.
Nice to have
- Transparent or textured backgrounds that can encompass any or all part of the banner such as a cutting board, shadows, abstract, etc to show depth are a plus.
- Use of vectors or objects such as ribbons or shapes to encapsulate the 'flavor texts' are also encouraged.

```html
<!DOCTYPE html>
<html lang="en">
<head>
<meta charset="utf-8">
<title>Fried Catfish Banner</title>
<link href="https://fonts.googleapis.com/css2?family=Great+Vibes&family=Montserrat:wght@800&display=swap" rel="stylesheet">
<style>
  :root {
    --orange: #e8822a;
    --orange-light: #ef9236;
    --orange-deep: #e47622;
    --yellow: #f7d21c;
    --yellow-light: #fbe03a;
    --yellow-mid: #f8c818;
    --amber: #f3a81a;
    --amber-light: #f7bc2a;
    --red: #e2231a;
    --white: #ffffff;
    --blue: #1a9ad6;
    --panel: #f1f1f1;
    --panel-shade: #e4e4e4;
  }
  html, body { margin: 0; padding: 0; overflow: hidden; }
  body { width: 1200px; height: 1200px; background: var(--white); position: relative; }
  p, h1 { margin: 0; }
  .banner { position: absolute; left: 435px; top: 239px; width: 330px; height: 722px; background: radial-gradient(ellipse at 50% 45%, var(--panel), var(--panel-shade)); overflow: hidden; }
  .title-band { position: absolute; left: 0; top: 0; width: 330px; height: 86px; background: radial-gradient(ellipse at 50% 50%, var(--orange-light), var(--orange)); display: flex; align-items: center; justify-content: center; }
  .title { font-family: 'Great Vibes', cursive; font-size: 58px; font-weight: 400; color: var(--white); line-height: 1; -webkit-text-stroke: 1.2px var(--white); padding-top: 4px; }
  .silver-rule { position: absolute; left: 0; top: 86px; width: 330px; height: 10px; background: linear-gradient(#fafafa, #bdbdbd); box-shadow: 0 2px 3px #0002; }
  .photo { position: absolute; left: 40px; top: 120px; width: 240px; height: 240px; border-radius: 50%; background: radial-gradient(circle at 45% 45%, #d08a3a, #a35f22 60%, #e6b45a); border: 8px solid #d8d8d8; box-sizing: border-box; box-shadow: 0 3px 6px #0003; }
  .fish-art { position: absolute; left: 192px; top: 306px; width: 124px; height: 118px; border-radius: 20px; background: linear-gradient(160deg, #b9b8aa, #7e7d6d); }
  .tagline { position: absolute; left: 34px; top: 352px; width: 120px; font-family: 'Great Vibes', cursive; color: var(--blue); font-size: 36px; line-height: 0.95; transform: rotate(-10deg); text-align: center; -webkit-text-stroke: 0.8px var(--blue); }
  .line { position: absolute; left: 0; width: 330px; display: flex; align-items: center; justify-content: center; font-family: 'Montserrat', sans-serif; font-weight: 800; text-transform: uppercase; text-align: center; box-sizing: border-box; }
  .scratch { top: 441px; height: 32px; color: var(--orange-deep); font-size: 17px; }
  .fillets { top: 484px; height: 54px; background: linear-gradient(var(--yellow-light), var(--yellow-mid)); color: var(--orange-deep); font-size: 16px; }
  .best { top: 539px; height: 55px; background: linear-gradient(var(--yellow-light), var(--yellow)); color: var(--red); font-size: 16px; }
  .pound { top: 595px; height: 52px; background: linear-gradient(var(--amber-light), var(--amber)); color: var(--white); font-size: 13.5px; }
  .served { top: 648px; height: 74px; background: radial-gradient(ellipse at 50% 50%, var(--orange-light), var(--orange)); color: var(--white); font-size: 13.5px; line-height: 1.55; padding: 0 14px; }
  .sep { position: absolute; left: 0; width: 330px; height: 3px; background: linear-gradient(#fff8, #0003); }
</style>
</head>
<body>
  <div class="banner">
    <header class="title-band"><h1 class="title">Fried Catfish</h1></header>
    <div class="silver-rule"></div>
    <div class="photo" role="img" aria-label="Plate of breaded fried catfish fillets with fries and hush puppies"></div>
    <div class="fish-art" role="img" aria-label="Illustrated catfish"></div>
    <div class="tagline">Always<br>Fresh!</div>
    <p class="line scratch">Made from Scratch</p>
    <p class="line fillets">Hand-cut Fillets</p>
    <div class="sep" style="top:537px"></div>
    <p class="line best">The Best Catfish in Texas</p>
    <div class="sep" style="top:593px"></div>
    <p class="line pound">Also available by the pound!</p>
    <div class="sep" style="top:646px"></div>
    <p class="line served">Served with fries, hush puppies &amp;<br>a 32oz fountain drink</p>
  </div>
</body>
</html>
```